Glimmerseal pond linings website template

We need a template for our new website. Glimmerseal is currently marketed through www.tarpavale.com.au, and we are moving the pond/dam linings to a dedicated site www.glimmerseal.com.au

The site is essentially brochureware. The content (less landing page & photo gallery) is on the new site to give you a better idea of what we do. We are also on Facebook.com/glimmerseal

We are looking for a template/style which we can adapt to the different sections of the site as required. We also get a lot of phone/tablet visitors so an alternative mobile layout would be a bonus, but by no means required.

I am proficient in HTML/CSS & javascript so can code most designs thrown at me.

Any icons or interface fonts should be freely available web fonts where possible.

Target Market(s)

We are targeting both landscape professionals (design & construction) as well as the DIY market for ponds/wateragrdens.

Industry/Entity Type

Moving

Requirements
Must have
• We need a design (preferably layered PSD or AI) as basis for our overall site look and feel. Fonts/iconography/layout are where we are lacking. We can do the HTML/CSS/JS/PHP internally.
Nice to have
• A style guide either in file or separate would be nice.
Layers with effect (i.e.. :hover, CSS3 transition endpoints, etc)

```html
<!DOCTYPE html>
<html lang="en">
<head>
<meta charset="utf-8">
<title>Glimmerseal – Custom made liners</title>
<link href="https://fonts.googleapis.com/css2?family=Questrial&family=Arimo:wght@400;700&family=Roboto+Condensed:wght@300&display=swap" rel="stylesheet">
<style>
:root{
  --nav-green:#6e9d2f;
  --text-green:#6aa022;
  --lime:#c3d32a;
  --navy:#14397a;
  --forest:#16703f;
  --grey-panel:#ebebeb;
  --body:#333;
  --muted:#666;
  --rule:#bdbdbd;
  --icon-grey:#9a9a9a;
}
*{margin:0;padding:0;box-sizing:border-box}
html,body{width:752px;height:1200px;overflow:hidden;background:#fff}
body{position:relative;font-family:Arimo,Arial,sans-serif;color:var(--body)}
.abs{position:absolute}
.display{font-family:Questrial,"Century Gothic",sans-serif}

/* header */
.brand{left:27px;top:26px;display:flex;align-items:center;gap:10px}
.brand-mark{width:34px;height:34px;background:var(--nav-green)}
.brand-name{font-family:Questrial,sans-serif;font-size:31px;color:var(--forest);letter-spacing:1px}
.contact-now{right:35px;top:19px;text-align:right;color:var(--navy);font-family:Questrial,sans-serif}
.contact-now .label{font-size:14px;letter-spacing:.5px}
.contact-now .phone{font-size:19px;display:flex;align-items:center;justify-content:flex-end;gap:3px}
.tagline{right:32px;top:75px;font-family:Questrial,sans-serif;color:var(--forest);font-size:15px}

/* nav */
.main-nav{left:27px;top:97px;width:696px;height:25px;background:var(--nav-green);display:flex;align-items:center;font-size:11px;color:#fff}
.main-nav span{position:absolute}

/* hero */
.hero{left:27px;top:122px;width:696px;height:319px;background:linear-gradient(100deg,#3d5a2c 0%,#6f8f4a 25%,#9aa9a0 40%,#4e6a36 60%,#7fa33d 80%,#3e5a28 100%)}
.hero-dots{right:44px;top:420px;display:flex;gap:7px}
.hero-dots i{width:11px;height:11px;border-radius:50%;background:#111}
.hero-dots i:first-child{background:#fff}

/* why */
.why-title{left:27px;top:462px;font-size:32px;color:var(--navy);letter-spacing:-.5px}
.why-title b{font-family:Arimo,sans-serif;font-weight:700;letter-spacing:-1px}
.why-copy{left:27px;top:509px;width:400px;font-size:10.6px;line-height:13.4px;color:#222}
.styles-title{left:27px;top:587px;font-size:28px;color:var(--navy);letter-spacing:-.5px}
.styles-list{left:27px;top:633px;list-style:none}
.styles-list li{display:flex;align-items:center;height:37.5px;font-family:Questrial,sans-serif;font-size:22px;color:var(--text-green);letter-spacing:-.3px}
.styles-list .num{width:30px;height:30px;border-radius:50%;background:var(--lime);color:#fff;font-size:20px;display:flex;align-items:center;justify-content:center;margin-right:12px}

/* happenings */
.happ-title{left:475px;top:462px;font-size:31px;color:var(--forest);letter-spacing:-.5px}
.happ-item{left:477px;width:248px;height:100px;border-bottom:1px solid var(--rule)}
.happ-thumb{position:absolute;left:0;top:0;width:89px;height:70px}
.happ-text{position:absolute;left:97px;top:-2px;width:153px}
.happ-text h3{font-weight:400;font-size:11.2px;color:var(--text-green);margin-bottom:2px}
.happ-text p{font-size:8.8px;line-height:11px;color:var(--muted)}
.happ-text a{display:block;font-size:8px;color:var(--text-green);text-decoration:none;margin-top:3px}

/* prepare */
.prepare{left:27px;top:808px;width:698px;height:232px;background:var(--grey-panel)}
.prepare-title{left:57px;top:826px;font-size:30px;color:var(--forest);letter-spacing:-.5px}
.step{top:888px;width:140px;text-align:center}
.step svg{display:block;margin:0 auto}
.step span{display:block;margin-top:10px;font-family:Questrial,sans-serif;font-size:10.5px;color:var(--text-green)}

/* footer */
.foot-h{top:1061px;font-size:13.5px;font-weight:700;color:#333;letter-spacing:.3px}
.foot-links{top:1085px;font-size:8.8px;line-height:11.1px;color:#555;list-style:none}
.foot-news{left:340px;top:1081px;width:200px}
.foot-news h4{font-size:10.2px;color:#444;margin-bottom:11px}
.foot-news p{font-size:8.8px;line-height:11.4px;color:#555}
.foot-news a{display:block;margin-top:6px;font-size:9.5px;color:var(--text-green);text-decoration:none}
.socials{left:585px;top:1083px;display:flex;gap:8px}
.socials i{width:21px;height:21px;border-radius:50%;background:var(--icon-grey)}
.foot-address{left:587px;top:1111px;font-size:9px;line-height:11px;color:#333}
.foot-phone{left:585px;top:1135px;display:flex;align-items:center;gap:5px;font-family:"Roboto Condensed",sans-serif;font-weight:300;font-size:19px;color:#888}
</style>
</head>
<body>

<header>
  <div class="abs brand"><span class="brand-mark"></span><span class="brand-name">GLIMMERSEAL</span></div>
  <div class="abs contact-now">
    <div class="label">CONTACT US NOW</div>
    <div class="phone">
      <svg width="12" height="12" viewBox="0 0 24 24" aria-hidden="true"><path d="M5 2h4l2 5-3 2c1 3 3 5 6 6l2-3 5 2v4c0 1-1 2-2 2C10 20 4 14 3 4c0-1 1-2 2-2z" fill="var(--navy)"/></svg>1300 555 218
    </div>
  </div>
  <div class="abs tagline">Custom made liners for ponds, pools &amp; watergardens.</div>
</header>

<nav class="abs main-nav">
  <span style="left:25px">Home</span>
  <span style="left:89px">About Us</span>
  <span style="left:169px">Happenings</span>
  <span style="left:263px">Gallery</span>
  <span style="left:333px">Liner Styles</span>
  <span style="left:425px">Preparation</span>
  <span style="left:517px">Installation</span>
  <span style="left:605px">Contact Us</span>
</nav>

<div class="abs hero" role="img" aria-label="Rainforest waterfall cascading over rocks into a pond, framed by tree ferns and a wooden ladder"></div>
<div class="abs hero-dots"><i></i><i></i><i></i><i></i></div>

<h1 class="abs why-title display">Why hire GLIMMER<b>SEAL</b>?</h1>
<p class="abs why-copy">All Glimmerseal pond liners are guaranteed for twenty years. They will accommodate fountains, waterfalls, drains and overflows, all which are easily installed. Glimmerseal pond liners will fit any shaped pond, pool, or water garden you can imagine – including curved profile walls and acute angles.</p>

<h2 class="abs styles-title display">Our LINER Styles</h2>
<ol class="abs styles-list">
  <li><span class="num">1</span>flat sheet liners</li>
  <li><span class="num">2</span>composite liners</li>
  <li><span class="num">3</span>profile liners</li>
  <li><span class="num">4</span>special project liners</li>
</ol>

<h2 class="abs happ-title display">HAPPENINGS</h2>
<article class="abs happ-item" style="top:513px">
  <div class="happ-thumb" role="img" aria-label="Show garden with a rust-red sculpture among green plantings" style="background:linear-gradient(135deg,#7a4a35,#a6765a 40%,#6f8d4a)"></div>
  <div class="happ-text"><h3>Ashgrove 2013 – Best In Show</h3><p>The 2013 Australian entry to the Ashgrove Flower Show, was designed and built by award winning designer Harlan Brooke.</p><a href="#">read more</a></div>
</article>
<article class="abs happ-item" style="top:613px">
  <div class="happ-thumb" role="img" aria-label="Still reflecting pool surrounded by tall trees" style="background:linear-gradient(180deg,#8a9a6a,#4d5a38 55%,#2c3424)"></div>
  <div class="happ-text"><h3>Ordered Nature – RGFS 2013</h3><p>This year we were asked to assist a new entrant, Dorian Vallis, with his first Riverside Garden and Flower Show ...</p><a href="#">read more</a></div>
</article>
<article class="abs happ-item" style="top:713px">
  <div class="happ-thumb" role="img" aria-label="Backyard garden with pink walls and a reflecting pool" style="background:linear-gradient(180deg,#c07890,#8d6a6e 45%,#6a5048)"></div>
  <div class="happ-text"><h3>Two gardens in one backyard.</h3><p>Why have one backyard garden when you can have two? This question was the inspiration for the latest creation from Felix Ardmore ...</p><a href="#">read more</a></div>
</article>

<section class="abs prepare"></section>
<h2 class="abs prepare-title display">How we prepare</h2>

<div class="abs step" style="left:22px">
  <svg width="80" height="80" viewBox="0 0 80 80" aria-hidden="true"><circle cx="40" cy="40" r="38" fill="var(--nav-green)" stroke="#fff" stroke-width="2"/><circle cx="40" cy="40" r="39.5" fill="none" stroke="var(--nav-green)"/><rect x="20" y="27" width="40" height="26" fill="none" stroke="#fff" stroke-width="3"/><path d="M36 34h18M36 40h18M36 46h14" stroke="#fff" stroke-width="2"/><circle cx="28" cy="42" r="4" fill="#fff"/></svg>
  <span>REGULATIONS</span>
</div>
<div class="abs step" style="left:161px">
  <svg width="80" height="80" viewBox="0 0 80 80" aria-hidden="true"><circle cx="40" cy="40" r="38" fill="var(--nav-green)" stroke="#fff" stroke-width="2"/><circle cx="40" cy="40" r="39.5" fill="none" stroke="var(--nav-green)"/><path d="M20 52V26h8l12 18" fill="none" stroke="#fff" stroke-width="3"/><rect x="40" y="38" width="16" height="10" fill="#fff"/><rect x="34" y="50" width="26" height="6" rx="3" fill="#fff"/></svg>
  <span>EXCAVATION</span>
</div>
<div class="abs step" style="left:308px">
  <svg width="80" height="80" viewBox="0 0 80 80" aria-hidden="true"><circle cx="40" cy="40" r="38" fill="var(--nav-green)" stroke="#fff" stroke-width="2"/><circle cx="40" cy="40" r="39.5" fill="none" stroke="var(--nav-green)"/><rect x="24" y="26" width="28" height="28" rx="3" fill="none" stroke="#fff" stroke-width="4"/><path d="M34 26v-4h8v4" fill="none" stroke="#fff" stroke-width="3"/><path d="M52 52h10M55 52v-3M58 52v-3" stroke="#fff" stroke-width="2"/></svg>
  <span>MEASURING</span>
</div>
<div class="abs step" style="left:449px">
  <svg width="80" height="80" viewBox="0 0 80 80" aria-hidden="true"><circle cx="40" cy="40" r="38" fill="var(--nav-green)" stroke="#fff" stroke-width="2"/><circle cx="40" cy="40" r="39.5" fill="none" stroke="var(--nav-green)"/><ellipse cx="40" cy="46" rx="16" ry="7" fill="#fff"/><circle cx="30" cy="34" r="3" fill="#fff"/><circle cx="44" cy="30" r="4" fill="#fff"/><circle cx="54" cy="36" r="2.5" fill="#fff"/><circle cx="24" cy="42" r="2" fill="#fff"/></svg>
  <span>OVERFLOW &amp; FILLING</span>
</div>
<div class="abs step" style="left:584px">
  <svg width="80" height="80" viewBox="0 0 80 80" aria-hidden="true"><circle cx="40" cy="40" r="38" fill="var(--nav-green)" stroke="#fff" stroke-width="2"/><circle cx="40" cy="40" r="39.5" fill="none" stroke="var(--nav-green)"/><circle cx="40" cy="40" r="16" fill="none" stroke="#fff" stroke-width="5"/><path d="M29 29l22 22" stroke="#fff" stroke-width="5"/></svg>
  <span>SAFETY</span>
</div>

<footer>
  <h4 class="abs foot-h" style="left:29px">NAVIGATION</h4>
  <ul class="abs foot-links" style="left:29px"><li>Home</li><li>About Us</li><li>Happenings</li><li>Gallery</li><li>Liner Styles</li><li>Preparation</li><li>Installation</li><li>Contact Us</li></ul>
  <ul class="abs foot-links" style="left:102px"><li>Flat Sheet Liners</li><li>Composite Liners</li><li>Profile Liners</li><li>Special Project Liners</li></ul>
  <ul class="abs foot-links" style="left:214px"><li>Regulations</li><li>Excavation</li><li>Measuring</li><li>Overflowing &amp; Filling</li><li>Safety</li></ul>

  <h4 class="abs foot-h" style="left:340px">HAPPENINGS</h4>
  <div class="abs foot-news"><h4>Ashgrove 2013 – Best In Show</h4><p>The 2013 Australian entry to the Ashgrove Flower Show, was designed and built by award winning designer Harlan Brooke.</p><a href="#">READ MORE</a></div>

  <h4 class="abs foot-h" style="left:585px">CONTACT US</h4>
  <div class="abs socials"><i></i><i></i><i></i><i></i><i></i></div>
  <div class="abs foot-address">Ferncliff Victoria, 3391<br>Australia</div>
  <div class="abs foot-phone">
    <svg width="18" height="18" viewBox="0 0 24 24" aria-hidden="true"><circle cx="12" cy="12" r="11" fill="none" stroke="#888" stroke-width="1.5"/><path d="M8 6h2l1 3-2 1c1 2 2 3 4 4l1-2 3 1v2c0 1-1 1-1 1C11 16 8 13 7 7c0-1 1-1 1-1z" fill="#888"/></svg>1300 555 218
  </div>
</footer>

</body>
</html>
```